2021 Summer Ads Whitmore Ash Custom Homes

We need a re-design of our summer ad run for our customer, Whitmore Ash Custom Homes. They are custom home builders in the mostly rural parts of West Virginia, USA. They are known for their "Forever Home" tagline. We'd like two designed ads with the main difference being just the custom home that's featured. These designs should be for a Google banner like 300 x 250 and square ad like 250 x 250. For inspiration please visit the Whitmore Ash Custom Homes website at www dot whitmoreashcustomhomes dot com

Target Market(s)

consumers / new home shoppers

Industry/Entity Type

Consumer

Requirements
Must have
• WACH logo
Price Lock Available!
Custom home pic
Learn more >
small QVTG logo mark

```html
<!DOCTYPE html>
<html lang="en">
<head>
<meta charset="utf-8">
<title>Whitmore Ash Custom Homes – Summer Ads</title>
<link rel="stylesheet" href="https://fonts.googleapis.com/css2?family=Poppins:wght@400;700&display=swap">
<style>
  :root {
    --page: #f4f4f4;
    --navy: #1f2535;
    --navy-soft: #2a3040;
    --red: #cc0000;
    --white: #ffffff;
    --sky: #4f8fce;
    --leaf: #3f7a32;
    --wall-white: #dfe3e6;
    --wall-red: #b3281a;
    --gravel: #8a8478;
  }
  html, body {
    margin: 0;
    width: 1200px;
    height: 1200px;
    overflow: hidden;
    background: var(--page);
    font-family: "Poppins", sans-serif;
  }
  .ad {
    position: absolute;
    left: 122px;
    width: 955px;
    height: 399px;
    display: block;
    filter: drop-shadow(8px 10px 10px rgba(0,0,0,0.22));
  }
  .ad--barn-white { top: 170px; }
  .ad--barn-red { top: 665px; }
  .ad text { font-family: "Poppins", sans-serif; fill: var(--white); }
  .brand-name { font-weight: 700; font-size: 44px; letter-spacing: 1px; }
  .brand-sub { font-weight: 400; font-size: 22px; letter-spacing: 4px; }
  .tagline { font-weight: 400; font-size: 48px; }
  .headline { font-weight: 700; font-size: 100px; }
  .cta-label { font-weight: 700; font-size: 28px; }
</style>
</head>
<body>

<svg class="ad ad--barn-white" viewBox="0 0 1538 643" role="group" aria-label="Whitmore Ash Custom Homes banner featuring a white barn-style home">
  <defs>
    <clipPath id="frame-a"><rect width="1538" height="643"/></clipPath>
    <linearGradient id="photo-white-barn" x1="0" y1="0" x2="0" y2="1">
      <stop offset="0" stop-color="var(--sky)"/>
      <stop offset="0.25" stop-color="var(--leaf)"/>
      <stop offset="0.4" stop-color="#3a3b36"/>
      <stop offset="0.55" stop-color="var(--wall-white)"/>
      <stop offset="0.85" stop-color="#7b7f82"/>
      <stop offset="1" stop-color="var(--gravel)"/>
    </linearGradient>
  </defs>
  <g clip-path="url(#frame-a)">
    <rect class="ad-base" width="1538" height="643" fill="var(--navy)"/>
    <rect class="top-gap" x="600" y="0" width="400" height="220" fill="var(--white)"/>
    <path class="text-panel" d="M0 0 H630 A130 130 0 0 1 760 130 V643 H0 Z" fill="var(--navy)"/>
    <circle class="accent-ring" cx="1190" cy="180" r="432" fill="var(--red)"/>
    <circle class="feature-photo" cx="1313" cy="177" r="440" fill="url(#photo-white-barn)" role="img" aria-label="Photo of a white board-and-batten custom home with dark roof, cupola and stone base"/>
  </g>
  <g class="brand">
    <rect x="88" y="58" width="22" height="22" fill="var(--white)"/>
    <text class="brand-name" x="122" y="80">WHITMORE ASH</text>
    <text class="brand-sub" x="90" y="130">CUSTOM HOMES</text>
  </g>
  <text class="tagline" x="88" y="265">Price Lock Available!</text>
  <text class="headline" x="84" y="366">CUSTOM</text>
  <text class="headline" x="84" y="452">HOME PIC</text>
  <g class="cta">
    <rect x="88" y="530" width="255" height="50" rx="18" fill="var(--red)"/>
    <text class="cta-label" x="215" y="565" text-anchor="middle">LEARN MORE</text>
  </g>
  <rect class="partner-badge" x="456" y="510" width="109" height="83" fill="var(--white)"/>
  <g class="dots" fill="var(--red)">
    <circle cx="774" cy="546" r="4"/><circle cx="794" cy="546" r="4"/><circle cx="814" cy="546" r="4"/>
    <circle cx="774" cy="568" r="4"/><circle cx="794" cy="568" r="4"/><circle cx="814" cy="568" r="4"/>
  </g>
</svg>

<svg class="ad ad--barn-red" viewBox="0 0 1538 643" role="group" aria-label="Whitmore Ash Custom Homes banner featuring a red barn-style home">
  <defs>
    <clipPath id="frame-b"><rect width="1538" height="643"/></clipPath>
    <linearGradient id="photo-red-barn" x1="0" y1="0" x2="0" y2="1">
      <stop offset="0" stop-color="#4d7a38"/>
      <stop offset="0.3" stop-color="var(--leaf)"/>
      <stop offset="0.42" stop-color="#9ea1a4"/>
      <stop offset="0.55" stop-color="var(--wall-red)"/>
      <stop offset="0.8" stop-color="var(--wall-red)"/>
      <stop offset="0.88" stop-color="var(--gravel)"/>
      <stop offset="1" stop-color="#d8d2c4"/>
    </linearGradient>
    <linearGradient id="backdrop-fade" x1="0" y1="0" x2="0" y2="1">
      <stop offset="0" stop-color="#2e3540"/>
      <stop offset="0.5" stop-color="#30374a"/>
      <stop offset="1" stop-color="#2b3142"/>
    </linearGradient>
  </defs>
  <g clip-path="url(#frame-b)">
    <rect class="ad-base" width="1538" height="643" fill="url(#backdrop-fade)"/>
    <rect class="top-gap" x="600" y="0" width="400" height="220" fill="#4f7a3c"/>
    <path class="text-panel" d="M0 0 H630 A130 130 0 0 1 760 130 V643 H0 Z" fill="url(#backdrop-fade)" role="img" aria-label="Faded photo of a custom home among trees"/>
    <circle class="accent-ring" cx="1190" cy="180" r="432" fill="var(--red)"/>
    <circle class="feature-photo" cx="1313" cy="177" r="440" fill="url(#photo-red-barn)" role="img" aria-label="Photo of a red board-and-batten custom home with grey roof, cupola and white trim"/>
  </g>
  <g class="brand">
    <rect x="88" y="58" width="22" height="22" fill="var(--white)"/>
    <text class="brand-name" x="122" y="80">WHITMORE ASH</text>
    <text class="brand-sub" x="90" y="130">CUSTOM HOMES</text>
  </g>
  <text class="tagline" x="88" y="265">Price Lock Available!</text>
  <text class="headline" x="84" y="366">CUSTOM</text>
  <text class="headline" x="84" y="452">HOME PIC</text>
  <g class="cta">
    <rect x="88" y="530" width="255" height="50" rx="18" fill="var(--red)"/>
    <text class="cta-label" x="215" y="565" text-anchor="middle">LEARN MORE</text>
  </g>
  <rect class="partner-badge" x="456" y="510" width="109" height="83" fill="var(--white)"/>
  <g class="dots" fill="var(--red)">
    <circle cx="774" cy="546" r="4"/><circle cx="794" cy="546" r="4"/><circle cx="814" cy="546" r="4"/>
    <circle cx="774" cy="568" r="4"/><circle cx="794" cy="568" r="4"/><circle cx="814" cy="568" r="4"/>
  </g>
</svg>

</body>
</html>
```